Educational outcome management software startup firm needs a graphic design

Our software startup firm, Kravix Metric Systems recently purchased a beautiful logo from Plumwerk (uploaded file). We are now looking for a graphic design to be used in the marketing activities of Kravix Metric Systems. See the uploaded picture of what a sketch of the graphic we are looking for.

```html
<!DOCTYPE html>
<html lang="en">
<head>
<meta charset="utf-8">
<title>Learner Wheel of Success</title>
<link href="https://fonts.googleapis.com/css2?family=Montserrat:wght@600;700;800;900&display=swap" rel="stylesheet">
<style>
  :root {
    --navy: #1d3461;
    --red: #cf3f35;
    --pink: #f1c6c3;
    --grey-line: #c9ccd1;
    --page: #f2f3f5;
    --paper: #ffffff;
  }
  html, body {
    margin: 0;
    padding: 0;
    width: 1200px;
    height: 3398px;
    overflow: hidden;
    background: var(--page);
    font-family: "Montserrat", Arial, sans-serif;
  }
  .poster {
    position: absolute;
    left: 50px;
    top: 989px;
    width: 1100px;
    height: 1420px;
    background: var(--paper);
    box-shadow: 0 6px 24px rgba(0, 0, 0, 0.12);
  }
  .poster svg { display: block; width: 100%; height: 100%; }
  .title-top { fill: var(--red); font-weight: 800; font-size: 58px; }
  .title-main { fill: var(--navy); font-weight: 900; font-size: 126px; }
  .label { fill: var(--navy); font-weight: 700; font-size: 11px; text-anchor: middle; }
  .label-left { text-anchor: start; }
  .center-label { fill: #fff; font-weight: 700; font-size: 15px; text-anchor: middle; }
  .ring-outer { fill: none; stroke: var(--red); stroke-width: 3; }
  .ring-outer-shadow { fill: none; stroke: var(--grey-line); stroke-width: 1; }
  .ring-middle { fill: none; stroke: var(--navy); stroke-width: 3; }
  .ring-inner-band { fill: none; stroke: var(--pink); stroke-width: 12; }
  .ring-inner-line { fill: none; stroke: var(--red); stroke-width: 2.5; }
  .stop-dot { fill: var(--red); stroke: #fff; stroke-width: 1.5; }
  .node { fill: #fff; stroke-width: 3; }
  .node-red { stroke: var(--red); }
  .node-navy { stroke: var(--navy); }
  .node-icon-red { fill: var(--red); }
  .node-icon-navy { fill: var(--navy); }
  .mask { fill: #fff; }
  .brand-name { fill: var(--navy); font-weight: 800; font-size: 22px; text-anchor: start; }
  .brand-mark { fill: var(--red); }
  .base-band { fill: var(--navy); }
</style>
</head>
<body>
<div class="poster">
  <svg viewBox="0 0 786 1015" xmlns="http://www.w3.org/2000/svg">
    <defs>
      <radialGradient id="hub-glow" cx="50%" cy="50%" r="50%">
        <stop offset="70%" stop-color="#1d3461" stop-opacity="0.55"/>
        <stop offset="100%" stop-color="#1d3461" stop-opacity="0"/>
      </radialGradient>
    </defs>

    <!-- Heading -->
    <text class="title-top" x="76" y="85" textLength="634" lengthAdjust="spacingAndGlyphs">LEARNER WHEEL OF</text>
    <text class="title-main" x="85" y="193" textLength="618" lengthAdjust="spacingAndGlyphs">SUCCESS</text>

    <!-- Outer ring: stakeholders -->
    <circle class="ring-outer-shadow" cx="400" cy="560" r="294"/>
    <circle class="ring-outer" cx="400" cy="560" r="300"/>
    <rect class="mask" x="660" y="596" width="80" height="56"/>

    <!-- Middle ring: milestones -->
    <path class="ring-middle" d="M453.2 346.5 A220 220 0 0 1 555.6 404.4"/>
    <path class="ring-middle" d="M582.4 437 A220 220 0 0 1 619.5 544.7"/>
    <path class="ring-middle" d="M605.4 638.8 A220 220 0 0 1 445.7 775.2"/>
    <path class="ring-middle" d="M339.4 775.5 A220 220 0 0 1 196 642.4"/>
    <path class="ring-middle" d="M180.5 544.6 A220 220 0 0 1 219.8 433.8"/>
    <path class="ring-middle" d="M250 399.1 A220 220 0 0 1 343.1 347.5"/>
    <g class="milestone-stops">
      <circle class="stop-dot" cx="453.2" cy="346.5" r="3.5"/>
      <circle class="stop-dot" cx="343.1" cy="347.5" r="3.5"/>
      <circle class="stop-dot" cx="555.6" cy="404.4" r="3.5"/>
      <circle class="stop-dot" cx="582.4" cy="437" r="3.5"/>
      <circle class="stop-dot" cx="619.5" cy="544.7" r="3.5"/>
      <circle class="stop-dot" cx="605.4" cy="638.8" r="3.5"/>
      <circle class="stop-dot" cx="445.7" cy="775.2" r="3.5"/>
      <circle class="stop-dot" cx="339.4" cy="775.5" r="3.5"/>
      <circle class="stop-dot" cx="196" cy="642.4" r="3.5"/>
      <circle class="stop-dot" cx="180.5" cy="544.6" r="3.5"/>
      <circle class="stop-dot" cx="219.8" cy="433.8" r="3.5"/>
      <circle class="stop-dot" cx="250" cy="399.1" r="3.5"/>
    </g>

    <!-- Inner ring: skills -->
    <circle class="ring-inner-band" cx="400" cy="560" r="140"/>
    <circle class="ring-inner-line" cx="400" cy="560" r="133"/>
    <rect class="mask" x="350" y="398" width="102" height="32"/>
    <rect class="mask" x="340" y="664" width="122" height="46"/>

    <!-- Hub -->
    <circle cx="400" cy="560" r="112" fill="url(#hub-glow)"/>
    <circle cx="400" cy="560" r="85" fill="var(--navy)"/>
    <circle cx="400" cy="560" r="75" fill="none" stroke="#fff" stroke-width="2"/>
    <circle cx="400" cy="524" r="20" fill="#ffffff" fill-opacity="0.85" role="img" aria-label="Graduate student icon"/>
    <text class="center-label" x="400" y="578">LEARNER/</text>
    <text class="center-label" x="400" y="596">STUDENT</text>

    <!-- Skill labels -->
    <text class="label" x="401" y="413">READING</text>
    <text class="label" x="401" y="426">SKILLS</text>
    <text class="label" x="279" y="483">STEM</text>
    <text class="label" x="279" y="496">SKILLS</text>
    <text class="label" x="530" y="483">WRITING</text>
    <text class="label" x="530" y="496">SKILLS</text>
    <text class="label" x="267" y="615">SOCIAL</text>
    <text class="label" x="267" y="628">SKILLS</text>
    <text class="label" x="529" y="615">STUDY</text>
    <text class="label" x="529" y="628">SKILLS</text>
    <text class="label" x="401" y="683">INFORMATION</text>
    <text class="label" x="401" y="696">TECHNOLOGY</text>
    <text class="label" x="401" y="709">SKILLS</text>

    <!-- Milestone labels -->
    <text class="label" x="394" y="340">HIGH SCHOOL</text>
    <text class="label" x="394" y="353">GRADUATION</text>
    <text class="label" x="570" y="422">EMPLOYMENT</text>
    <text class="label" x="245" y="422">ENTREPRENEUR</text>
    <text class="label" x="185" y="567">GRADUATION</text>
    <text class="label" x="185" y="580">FROM</text>
    <text class="label" x="185" y="593">HIGHER</text>
    <text class="label" x="185" y="606">EDUCATION</text>
    <text class="label" x="618" y="567">ADMISSION</text>
    <text class="label" x="618" y="580">IN TO</text>
    <text class="label" x="618" y="593" letter-spacing="-0.4">POST-SECONDARY</text>
    <text class="label" x="618" y="606">INSTITUTION</text>
    <text class="label" x="394" y="772">COMPLETION OF</text>
    <text class="label" x="394" y="785">ELEMENTARY</text>
    <text class="label" x="394" y="798">SCHOOL</text>

    <!-- Stakeholder nodes -->
    <g class="stakeholders">
      <circle class="node node-red" cx="400" cy="260" r="29"/>
      <circle class="node-icon-red" cx="400" cy="260" r="15" role="img" aria-label="Parent and guardian icon"/>
      <circle class="node node-navy" cx="612" cy="348" r="29"/>
      <circle class="node-icon-navy" cx="612" cy="348" r="15" role="img" aria-label="Employer icon"/>
      <circle class="node node-red" cx="700" cy="560" r="29"/>
      <circle class="node-icon-red" cx="700" cy="560" r="15" role="img" aria-label="Post-secondary education icon"/>
      <circle class="node node-navy" cx="612" cy="772" r="29"/>
      <circle class="node-icon-navy" cx="612" cy="772" r="15" role="img" aria-label="Government building icon"/>
      <circle class="node node-red" cx="400" cy="860" r="29"/>
      <circle class="node-icon-red" cx="400" cy="860" r="15" role="img" aria-label="Market place storefront icon"/>
      <circle class="node node-navy" cx="188" cy="772" r="29"/>
      <circle class="node-icon-navy" cx="188" cy="772" r="15" role="img" aria-label="School administrator icon"/>
      <circle class="node node-red" cx="100" cy="560" r="29"/>
      <circle class="node-icon-red" cx="100" cy="560" r="15" role="img" aria-label="School counselor icon"/>
      <circle class="node node-navy" cx="188" cy="348" r="29"/>
      <circle class="node-icon-navy" cx="188" cy="348" r="15" role="img" aria-label="Teacher icon"/>
    </g>

    <!-- Stakeholder labels -->
    <text class="label" x="400" y="220">PARENT/GUARDIAN</text>
    <text class="label" x="703" y="357">EMPLOYER</text>
    <text class="label" x="98" y="370">TEACHER</text>
    <text class="label" x="101" y="612">SCHOOL</text>
    <text class="label" x="101" y="625">COUNSELOR</text>
    <text class="label" x="698" y="610">POST-</text>
    <text class="label" x="698" y="623">SECONDARY</text>
    <text class="label" x="698" y="636">EDUCATION</text>
    <text class="label" x="698" y="649">SYSTEMS</text>
    <text class="label" x="113" y="805">SCHOOL</text>
    <text class="label" x="113" y="818">ADMINISTRATOR</text>
    <text class="label" x="656" y="814">GOVERNMENT</text>
    <text class="label" x="401" y="915">INTERNATION</text>
    <text class="label" x="401" y="928">MARKET PLACE</text>

    <!-- Brand -->
    <g class="brand">
      <rect class="brand-mark" x="268" y="962" width="14" height="14"/>
      <text class="brand-name" x="290" y="977">Kravix Metric Systems</text>
    </g>
    <rect class="base-band" x="0" y="1009" width="786" height="6"/>
  </svg>
</div>
</body>
</html>
```